Modern Minimalistic Supplement Label

Opportunity for recurring projects with a growing company. We have provided a detailed creative brief and all necessary files and guidelines. If you have any questions we will be closely monitoring the discussion board and email provided.

THE NAMES LISTED IN THE BRIEF ARE DIFFERENT FROM THE LABEL TEMPLATES. This is a private label brand. The label templates given are generic so please examine the entire brief before starting.

Use the PSD mockups attached and pair the labels with the correct bottles.

Do not use an entirely white background.

This could be excellent portfolio material.

Start by looking at the "CREATIVE_BRIEF" file. Logo files are contained in the "58213907" zip file.

UPDATE* Use the following business address for the "manufactured for" box on the labels.

Fernwick
4817 Larkmoor Ave. #2209
Ann Arbor MI 48196

Target Market(s)

All information provided in "CREATIVE_BRIEF" file.

Industry/Entity Type

Supplement

Requirements
Must have
• All information provided in "CREATIVE_BRIEF" file.
Nice to have
Should not have

```html
<!DOCTYPE html>
<html lang="en">
<head>
<meta charset="utf-8">
<title>Fernwick Amino Surge – Raspberry Iced Tea Label</title>
<link rel="stylesheet" href="https://fonts.googleapis.com/css2?family=Bebas+Neue&family=Roboto:wght@400;500&family=Roboto+Condensed:wght@700&family=Montserrat:wght@600&family=Dancing+Script:wght@500&display=swap">
<style>
  :root {
    --canvas: #f2f2f2;
    --label-black: #0e0e0f;
    --panel-dark: #232325;
    --panel-mid: #303033;
    --white: #ffffff;
    --soft-white: #e9e9e9;
    --raspberry: #d3155e;
    --raspberry-light: #e2407c;
  }
  * { margin: 0; padding: 0; box-sizing: border-box; }
  html, body {
    width: 1200px;
    height: 1200px;
    overflow: hidden;
    background: var(--canvas);
  }
  .label {
    position: absolute;
    left: 120px;
    top: 220px;
    width: 960px;
    height: 760px;
    background: var(--label-black);
    color: var(--white);
  }
  .texture-panel {
    position: absolute;
    left: 150px;
    top: 80px;
    width: 660px;
    height: 600px;
    background: linear-gradient(135deg, var(--panel-dark) 0%, var(--panel-mid) 45%, var(--panel-dark) 100%);
    opacity: 0.9;
  }
  .brand {
    position: absolute;
    top: 220px;
    width: 100%;
    display: flex;
    justify-content: center;
    align-items: center;
    gap: 16px;
  }
  .brand-mark {
    width: 18px;
    height: 18px;
    background: var(--white);
  }
  .brand-name {
    font-family: "Montserrat", sans-serif;
    font-weight: 600;
    font-size: 52px;
    letter-spacing: 6px;
    color: var(--white);
  }
  .product-name {
    position: absolute;
    top: 370px;
    width: 100%;
    text-align: center;
    font-family: "Bebas Neue", sans-serif;
    font-size: 140px;
    line-height: 1;
    letter-spacing: 2px;
    color: var(--white);
  }
  .flavor-band {
    position: absolute;
    top: 520px;
    left: 0;
    width: 100%;
    height: 58px;
    background: linear-gradient(90deg, var(--raspberry-light) 0%, var(--raspberry) 40%, var(--raspberry) 100%);
    display: flex;
    justify-content: center;
    align-items: center;
  }
  .flavor-name {
    font-family: "Roboto Condensed", sans-serif;
    font-weight: 700;
    font-size: 34px;
    letter-spacing: 4px;
    color: var(--white);
  }
  .band-rule {
    position: absolute;
    top: 592px;
    left: 0;
    width: 100%;
    height: 3px;
    background: var(--soft-white);
  }
  .flavor-note {
    position: absolute;
    top: 610px;
    width: 100%;
    text-align: center;
    font-family: "Dancing Script", cursive;
    font-weight: 500;
    font-size: 26px;
    color: var(--soft-white);
  }
  .net-weight {
    position: absolute;
    top: 670px;
    width: 100%;
    text-align: center;
    font-family: "Roboto", sans-serif;
    font-weight: 500;
    font-size: 27px;
    letter-spacing: 3px;
    color: var(--soft-white);
    white-space: nowrap;
  }
  .net-weight .divider { margin: 0 18px; }
</style>
</head>
<body>
  <main class="label">
    <div class="texture-panel" role="img" aria-label="Dark diagonal pinstripe texture panel"></div>

    <div class="brand">
      <span class="brand-mark"></span>
      <span class="brand-name">FERNWICK</span>
    </div>

    <h1 class="product-name">AMINO SURGE</h1>

    <div class="flavor-band">
      <span class="flavor-name">RASPBERRY ICED TEA</span>
    </div>
    <div class="band-rule"></div>

    <p class="flavor-note">Natural &amp; Artificial Flavor</p>

    <p class="net-weight">NET WT.&nbsp; 360 G ( 12.7 OZ )<span class="divider">|</span>DIETARY SUPPLEMENT</p>
  </main>
</body>
</html>
```